Company Brochure promoting our Managed Services Business (MSP)

Objective: Is the brochure meant to generate leads, educate potential clients, and promote our Managed Services Business.
Target Audience: is for Small to medium size business.
A managed service provider like Brillora Advisory Group handles a variety of different responsibilities for Business
. We oversee vital IT resources such as:
Email
Cloud integration
Data storage
Networking
Cybersecurity
File backup
Help desk services
Our firm also provides remote monitoring services and updates. As part of our managed service provider solutions, we will continually report on the performance and quality of your network. We can even help your organization acquire new hardware and software.
At Brillora Advisory Group we specialize in empowering commercial businesses with robust IT solutions tailored to enhance efficiency, security, and scalability. With years of expertise in Managed Services, we understand the unique challenges businesses face in today’s digital landscape.
Call-to-Action (CTA):
Encourage readers to contact you, visit your website, or schedule a consultation.
you can get an overview of BAG at www..brillorabag.example.
Layout: Opt for a clean, easy-to-read layout with well-defined sections.
Imagery:
Include professional photos, custom graphics, or icons that represent your services.
Avoid generic stock images when possible.
Format: Tri-fold, bi-fold, depending on the amount of information.
We would like to have a section of the "Five-Step" from our web site.
I have attached the Logos.
Target Market(s)
Small to Medium Business
Look and feel

```html
<!DOCTYPE html>
<html lang="en">
<head>
<meta charset="utf-8">
<title>Brillora Advisory Group – Managed Services Brochure</title>
<link rel="stylesheet" href="https://fonts.googleapis.com/css2?family=Montserrat:wght@400;500;600;700&family=Inter:wght@400;500;600;700&display=swap">
<style>
:root{
  --bg:#e8e8ea;
  --navy:#0f1c2e;
  --navy-deep:#091320;
  --ink:#1b1f24;
  --muted:#3a3f46;
  --lavender:#dfe1ea;
  --blush:#efe5e6;
  --teal:#1c5668;
  --teal-dark:#184b5b;
  --white:#ffffff;
  --black:#050607;
}
*{box-sizing:border-box;margin:0;padding:0}
html,body{width:1200px;height:3241px;overflow:hidden;background:var(--bg)}
body{font-family:"Inter",Arial,sans-serif;color:var(--ink);position:relative}
.spread{position:absolute;left:60px;width:1080px;height:837px;display:flex;box-shadow:0 6px 24px rgba(0,0,0,.12);background:var(--white)}
.spread--outside{top:560px}
.spread--inside{top:1760px}
.panel{width:360px;height:100%;position:relative;overflow:hidden}

/* brand lockup */
.brand{display:flex;align-items:center;gap:12px;position:absolute;top:36px;left:36px}
.brand__mark{width:46px;height:46px;background:var(--white);flex:none}
.brand__name{font-family:"Montserrat",Arial,sans-serif;font-weight:500;font-size:17px;line-height:1.05;color:var(--white);letter-spacing:.5px;text-transform:uppercase}

/* outside: why choose */
.why{background:var(--white)}
.why__title{font-family:"Montserrat",Arial,sans-serif;font-weight:700;font-size:21px;line-height:1.2;margin:48px 30px 0 34px}
.why__photo{position:absolute;top:132px;left:0;width:325px;height:382px;background:linear-gradient(160deg,#e9d9c8 0%,#a9a6a6 40%,#46505c 100%)}
.why__list{position:absolute;top:560px;left:34px;right:28px;list-style:none}
.why__item{display:flex;gap:16px;margin-bottom:22px}
.why__item svg{flex:none;width:34px;height:34px}
.why__item h4{font-size:14px;font-weight:700;margin-bottom:3px}
.why__item p{font-size:13.5px;line-height:1.3}

/* outside: contact */
.contact{background:radial-gradient(circle at 70% 70%,#2e4a66 0%,#15263a 45%,var(--navy-deep) 100%)}
.contact__cta{position:absolute;top:222px;left:0;right:0;text-align:center;font-family:"Montserrat",Arial,sans-serif;font-weight:600;font-size:23px;line-height:1.42;color:var(--white);text-transform:uppercase}
.contact__card{position:absolute;left:34px;right:34px;top:506px;bottom:0;background:var(--blush);text-align:center;padding-top:24px;font-size:13px;line-height:1.4}
.contact__label{font-size:9.5px;font-weight:700;text-transform:uppercase;letter-spacing:.4px;margin-top:18px}
.contact__label:first-child{margin-top:0}

/* outside: cover */
.cover{background:var(--white)}
.cover__photo{position:absolute;top:0;left:0;right:0;height:648px;background:radial-gradient(circle at 62% 32%,#6f8fb3 0%,#2d4664 28%,#12213a 60%,var(--navy-deep) 100%)}
.cover__title{position:absolute;top:492px;left:30px;right:8px;font-family:"Montserrat",Arial,sans-serif;font-weight:700;font-size:35px;line-height:1.14;color:var(--white);white-space:nowrap}
.cover__band{position:absolute;top:648px;left:0;right:0;height:120px;background:var(--black);color:var(--white);font-size:15px;font-weight:600;line-height:1.38;padding:24px 30px 0}
.cover__url{position:absolute;bottom:24px;left:0;right:0;text-align:center;font-weight:700;font-size:16px}

/* inside: header photo */
.inside-top{position:absolute;top:0;left:0;width:720px;height:176px;background:linear-gradient(100deg,#1a2640 0%,#3a4357 40%,#a68468 55%,#2a3447 75%,#15203a 100%);z-index:2}
.about{background:var(--lavender)}
.about__body{position:absolute;top:222px;left:34px;right:44px}
.section-title{font-family:"Montserrat",Arial,sans-serif;font-weight:700;font-size:22px;margin-bottom:36px}
.about h4{font-size:13.5px;font-weight:700;margin-bottom:12px}
.about p{font-size:13.5px;line-height:1.45;margin-bottom:26px}
.about__photo{position:absolute;bottom:0;left:0;right:0;height:197px;background:linear-gradient(170deg,#c7ced8 0%,#7d8fa6 45%,#2c3a52 100%)}

.services{background:var(--white)}
.services__body{position:absolute;top:222px;left:30px;right:30px}
.services .section-title{margin-left:10px;margin-bottom:28px}
.svc{display:flex;gap:14px;margin-bottom:22px}
.svc svg{flex:none;width:30px;height:30px;margin-top:2px}
.svc h4{font-size:13.5px;font-weight:700;margin-bottom:4px}
.svc p{font-size:12.5px;line-height:1.35}

.method{background:var(--teal);color:var(--white)}
.method__badge{position:absolute;top:24px;left:50%;transform:translateX(-50%);width:166px;height:166px;border-radius:50%;background:var(--white)}
.method__title{position:absolute;top:222px;left:30px;font-family:"Montserrat",Arial,sans-serif;font-weight:700;font-size:21px;line-height:1.2}
.method__list{position:absolute;top:302px;left:30px;right:24px;list-style:none}
.step{display:flex;gap:14px;margin-bottom:18px}
.step svg{flex:none;width:30px;height:30px}
.step h4{font-size:13.5px;font-weight:700;margin-bottom:3px}
.step p{font-size:12.5px;line-height:1.33}
.method__note{position:absolute;bottom:40px;left:30px;right:40px;font-size:12.5px;line-height:1.35}
</style>
</head>
<body>

<!-- Outside -->
<section class="spread spread--outside">
  <article class="panel why">
    <h2 class="why__title">Why Choose Brillora<br>Advisory Group?</h2>
    <div class="why__photo" role="img" aria-label="Photo of hands typing on a laptop with overlaid digital workflow graphics"></div>
    <ul class="why__list">
      <li class="why__item">
        <svg viewBox="0 0 34 34" fill="none" stroke="#1b1f24" stroke-width="1.6"><circle cx="17" cy="13" r="8"/><path d="M11 20l-3 10 5-2 3 4 1-6M23 20l3 10-5-2-3 4"/></svg>
        <div><h4>150+ Years of Expertise:</h4><p>A wealth of experience delivering innovative IT solutions.</p></div>
      </li>
      <li class="why__item">
        <svg viewBox="0 0 34 34" fill="none" stroke="#1b1f24" stroke-width="1.6"><rect x="3" y="14" width="12" height="12"/><rect x="19" y="4" width="12" height="12"/><path d="M15 20h6v-4"/></svg>
        <div><h4>Tailored Strategies:</h4><p>Personalized solutions designed to meet your unique business goals.</p></div>
      </li>
      <li class="why__item">
        <svg viewBox="0 0 34 34" fill="none" stroke="#1b1f24" stroke-width="1.6"><rect x="5" y="4" width="20" height="26" rx="2"/><path d="M9 11h12M9 16h12M9 21h7"/><circle cx="25" cy="24" r="5"/></svg>
        <div><h4>Long-Term Partnerships:</h4><p>We’re committed to your growth and success.</p></div>
      </li>
    </ul>
  </article>

  <article class="panel contact">
    <div class="brand"><span class="brand__mark"></span><span class="brand__name">Brillora<br>Advisory<br>Group</span></div>
    <h2 class="contact__cta">Get started<br>with Brillora<br>MSP services<br>today</h2>
    <div class="contact__card">
      <p class="contact__label">HQ Address</p>
      <p>210 Harbor Crest Way<br>Suite 40<br>Port Alder, FL 30000</p>
      <p class="contact__label">Locations</p>
      <p>Port Alder - Cedar Bay - Linwood<br>Maple Shore - Ridgefield</p>
      <p class="contact__label">Phone</p>
      <p>1-800-555-0142</p>
      <p class="contact__label">Email</p>
      <p>Sales@brillorabag.example</p>
    </div>
  </article>

  <article class="panel cover">
    <div class="cover__photo" role="img" aria-label="Photo of a hand touching a glowing digital interface in blue tones"></div>
    <div class="brand"><span class="brand__mark"></span><span class="brand__name">Brillora<br>Advisory<br>Group</span></div>
    <h1 class="cover__title">Empowering<br>Businesses in<br>the Digital Age</h1>
    <p class="cover__band">Your trusted partner in delivering innovative IT solutions, enhancing efficiency, and driving success.</p>
    <p class="cover__url">www.brillorabag.example</p>
  </article>
</section>

<!-- Inside -->
<section class="spread spread--inside">
  <div class="inside-top" role="img" aria-label="Photo of a business handshake with network lines overlay">
    <div class="brand"><span class="brand__mark"></span><span class="brand__name">Brillora<br>Advisory<br>Group</span></div>
  </div>

  <article class="panel about">
    <div class="about__body">
      <h2 class="section-title">About Us</h2>
      <h4>Empowering Your Digital Future</h4>
      <p>At Brillora Advisory Group, we transform businesses with cutting-edge technology solutions. Our expert consultants streamline operations, enhance security, and drive innovation, ensuring you stay ahead of the competition.</p>
      <h4>Empowering Your Digital Future</h4>
      <p>Our VisionTo empower businesses of all sizes with tailored IT solutions, fostering growth and success in an ever-evolving digital landscape.</p>
    </div>
    <div class="about__photo" role="img" aria-label="Photo of a team reviewing charts on a desk"></div>
  </article>

  <article class="panel services">
    <div class="services__body">
      <h2 class="section-title">Our Services</h2>
      <div class="svc"><svg viewBox="0 0 30 30" fill="none" stroke="#1b1f24" stroke-width="1.5"><circle cx="15" cy="12" r="6"/><path d="M3 24c4-4 8-4 12-2s8 2 12-2"/></svg><div><h4>Managed Services</h4><p>Leave your IT to the experts! We monitor and manage your networks, security, and software to keep your business running smoothly.</p></div></div>
      <div class="svc"><svg viewBox="0 0 30 30" fill="none" stroke="#1b1f24" stroke-width="1.5"><rect x="5" y="3" width="18" height="24" rx="2"/><path d="M9 10h10M9 15h10M9 20h6"/></svg><div><h4>Account Management</h4><p>Focus on growth while we handle RFPs, contracts, and service renewals with precision and expertise.</p></div></div>
      <div class="svc"><svg viewBox="0 0 30 30" fill="none" stroke="#1b1f24" stroke-width="1.5"><circle cx="15" cy="15" r="6"/><path d="M15 3v5M15 22v5M3 15h5M22 15h5M7 7l3 3M20 20l3 3M23 7l-3 3M7 23l3-3"/></svg><div><h4>Business Technologies</h4><p>Work smarter, not harder! We integrate advanced tools for efficiency, communication, security, and future-proofing.</p></div></div>
      <div class="svc"><svg viewBox="0 0 30 30" fill="none" stroke="#1b1f24" stroke-width="1.5"><rect x="3" y="5" width="24" height="16"/><path d="M10 27h10M15 21v6M8 12h8"/></svg><div><h4>Training &amp; Education</h4><p>Empower your team with tailored programs designed to enhance skills and boost performance.</p></div></div>
      <div class="svc"><svg viewBox="0 0 30 30" fill="none" stroke="#1b1f24" stroke-width="1.5"><circle cx="11" cy="11" r="6"/><circle cx="20" cy="20" r="6"/></svg><div><h4>Workflow Management</h4><p>Streamline your processes with intuitive tools for documentation, monitoring, and continuous improvement.</p></div></div>
    </div>
  </article>

  <article class="panel method">
    <div class="method__badge" aria-hidden="true"></div>
    <h2 class="method__title">Our Methodology:<br>Five-Step Growth Framework</h2>
    <ul class="method__list">
      <li class="step"><svg viewBox="0 0 30 30" fill="none" stroke="#fff" stroke-width="1.5"><rect x="4" y="4" width="18" height="22"/><circle cx="20" cy="19" r="5"/><path d="M24 23l4 4"/></svg><div><h4>Evaluate</h4><p>Analyze your current systems and gather insights to identify challenges and opportunities.</p></div></li>
      <li class="step"><svg viewBox="0 0 30 30" fill="none" stroke="#fff" stroke-width="1.5"><circle cx="15" cy="15" r="11"/><path d="M10 17l4-5 3 3 4-5"/></svg><div><h4>Enhance</h4><p>Optimize workflows, streamline inefficiencies, and implement best practices.</p></div></li>
      <li class="step"><svg viewBox="0 0 30 30" fill="none" stroke="#fff" stroke-width="1.5"><rect x="4" y="4" width="22" height="22"/><path d="M8 22l6-8 4 4 5-7"/></svg><div><h4>Engineer</h4><p>Design and structure tailored solutions aligned with your goals.</p></div></li>
      <li class="step"><svg viewBox="0 0 30 30" fill="none" stroke="#fff" stroke-width="1.5"><rect x="6" y="3" width="18" height="24" rx="2"/><path d="M10 15l3 3 6-7"/></svg><div><h4>Execute</h4><p>Implement strategies with precision and transparency, ensuring milestones are met.</p></div></li>
      <li class="step"><svg viewBox="0 0 30 30" fill="none" stroke="#fff" stroke-width="1.5"><path d="M15 4c6 4 6 10 0 14-6-4-6-10 0-14z"/><path d="M9 22c3 3 9 3 12 0M15 18v8"/></svg><div><h4>Evolve</h4><p>Adapt and innovate through continuous improvement and regular reviews.</p></div></li>
    </ul>
    <p class="method__note">Let Brillora’s proven methodology position your business for long-term success!</p>
  </article>
</section>

</body>
</html>
```